Print design needed to improve the layout and look of some existing documents

We need someone to take a couple of existing documents that we have and make them look much better using our existing logo and corporate colors etc. We require these to be delivered in a format that will allow our staff to edit the content as necessary via Microsoft word for conversion once finalized into a PDF. Ideally, we will also be able to use this as a newsletter template or for other documents that might be required in our business. www.calderfinch.com.au
Updates

Project Deadline Extended Reason: So far, I have only seen one design that I believe is quite good quality. Added Sunday, July 3, 2016

Target Market(s)

Business owners, executives, retirees

Industry/Entity Type

Financial Service

Font styles to use
Serif

Requirements
Must have
• Design that uses our existing branding and colors. It also needs to be ina form that we can edit the content / update easily. Ideally the format / layout could also be used for other documents such as short newsletters etc.
Nice to have
• Fresh, simple and crisp. Very professional looking.
Should not have
• strange fonts, weird layouts.

```html
<!DOCTYPE html>
<html lang="en">
<head>
<meta charset="utf-8">
<title>Privacy Policy Statement – Calder Finch</title>
<link href="https://fonts.googleapis.com/css2?family=Cinzel:wght@700&family=Didact+Gothic&display=swap" rel="stylesheet">
<style>
  :root {
    --ink: #3c3c3c;
    --heading: #3a3a3a;
    --green: #6cb33f;
    --blue: #1b98d5;
    --frame-a: #dcece6;
    --frame-b: #e9efe0;
    --page: #ffffff;
  }
  html, body { margin: 0; padding: 0; }
  body {
    width: 848px; height: 1200px; overflow: hidden; position: relative;
    background: linear-gradient(135deg, var(--frame-b), var(--frame-a) 50%, #d6e8e4);
    font-family: "Didact Gothic", "Century Gothic", sans-serif;
    color: var(--ink);
  }
  .sheet {
    position: absolute; left: 20px; top: 20px; width: 811px; height: 1168px;
    background: linear-gradient(180deg, var(--page) 0%, #fbfcfc 80%, #f3f6f6 100%);
  }
  .brand {
    position: absolute; left: 24px; top: 32px;
    display: flex; align-items: center; gap: 10px;
    font-size: 24px; color: #6a6a6a; letter-spacing: 1px;
  }
  .brand-dot { width: 14px; height: 14px; border-radius: 50%; background: var(--blue); }
  .section-title {
    position: absolute; margin: 0;
    font-family: "Cinzel", "Copperplate", serif; font-weight: 700;
    font-size: 22.5px; line-height: 25.5px; letter-spacing: 1.4px;
    color: var(--heading);
  }
  .rule { position: absolute; height: 6px; }
  .rule-left { background: linear-gradient(90deg, var(--green), var(--blue)); }
  .rule-right { background: linear-gradient(90deg, var(--blue), var(--green)); }
  .copy {
    position: absolute; width: 362px;
    font-size: 15.6px; line-height: 20.4px; text-align: justify;
  }
  .copy p { margin: 0 0 20.4px; }
  .copy p.tight { margin-bottom: 0; }
  .copy ul { list-style: none; margin: 0 0 20.4px; padding: 0; text-align: left; }
  .copy li::before { content: "• "; }
</style>
</head>
<body>
  <div class="sheet"></div>

  <div class="brand"><span class="brand-dot"></span>Calder Finch</div>

  <h2 class="section-title" style="left:44px; top:124px;">What&nbsp;&nbsp;information<br>do&nbsp;we&nbsp;collect&nbsp;and<br>how do we use it?</h2>
  <div class="rule rule-left" style="left:5px; top:210px; width:401px;"></div>

  <div class="copy" style="left:41px; top:238px;">
    <p>If you are acquiring or have acquired a service from Calder Finch Pty Ltd, we collect and hold your personal information for the purpose of providing you with relevant and accurate service and financial advice as well as managing and administering the service.</p>
    <p>This can include a broad range of information ranging from your name, postal and email address, date of birth, contact details and age to other information about your personal affairs including your financial details, tax file numbers or other information the organisation considers necessary.</p>
    <p class="tight">We may disclose the information that you provide to third party organisations where you have request that we liaise with or refer you to the organisations. This may include firms providing accounting, legal, credit, transactional banking, investment administration or insurance services.</p>
    <p>We may use your information to enable us to manage your ongoing requirements and our relationship with you. We may do so by mail or electronically unless you tell us that you do not wish to receive electronic communications.</p>
    <p>From time to time we may use your contact details to send you offers, updates, events, articles, newsletters or other information about services or events that we believe will be of interest to you.</p>
    <p>You can contact us at any time if you no longer wish us to do so.</p>
    <p>We may also use your information internally to help us improve our services and help resolve any problems.</p>
  </div>

  <h2 class="section-title" style="left:439px; top:124px;">What happens if you<br>don’t provide some<br>information to us?</h2>
  <div class="rule rule-right" style="left:437px; top:210px; width:411px;"></div>

  <div class="copy" style="left:439px; top:239px;">
    <p>If you do not provide us with some or all of the information that we ask for, we may not be able to accurately assess your situation and provide relevant and accurate financial advice.</p>
  </div>

  <h2 class="section-title" style="left:439px; top:412px;">How&nbsp;&nbsp;do&nbsp;&nbsp;we&nbsp;&nbsp;hold<br>and&nbsp;protect&nbsp;your<br>information?</h2>
  <div class="rule rule-right" style="left:437px; top:500px; width:411px;"></div>

  <div class="copy" style="left:439px; top:527px;">
    <p>We strive to maintain the relevance, reliability, accuracy, completeness and currency of the personal information we hold and to protect its privacy and security. We keep personal information only for as long as is reasonably necessary for the purpose for which it was collected or to comply with any applicable legal or ethical reporting or document retention requirements.</p>
    <p>We store information collected from you in different ways, including in paper and electronic form. The security of your personal information is important to us and we take reasonable steps to protect it from misuse and loss and unauthorised access, modification or disclosure.<br>Privacy Policy Statement – V2015</p>
    <p class="tight">Some of the ways we ensure that your information is safe are:</p>
    <ul>
      <li>confidentiality requirements for our employees</li>
      <li>security measures for systems access</li>
      <li>access control for our building</li>
    </ul>
    <p>We also maintain physical security over our paper and electronic data and premises, by using locks and security systems.</p>
  </div>
</body>
</html>
```